A label for my commercially sold local honey. This is a LABEL not a logo

3 inches high
2 inches wide

Target Market(s)

Customers who like "local" honey

Logo Text

Wildflower Honey -- 100% Pure & Unfiltered -- Florida

Logo styles of interest
Wordmark Logo
Requirements
Must have
• Wildflower Honey -- 100% Pure & Unfiltered -- Florida

Florida should be dominant

3 inches high / 2 inches wide

```html
<!DOCTYPE html>
<html lang="en">
<head>
<meta charset="utf-8">
<title>Wildflower Honey Label</title>
<link rel="stylesheet" href="https://fonts.googleapis.com/css2?family=Lobster&family=Oswald:wght@400;500;600;700&display=swap">
<style>
  :root {
    --label-yellow: #fdc96c;
    --comb-light: #fdd690;
    --honey-brown: #91501f;
    --ink-brown: #5a3213;
    --ribbon-brown: #a1581f;
    --ribbon-fold: #7d4014;
    --frame-white: #fff6e6;
    --art-warm: #e9a04a;
    --art-soft: #f6b960;
  }
  * { margin: 0; padding: 0; box-sizing: border-box; }
  html, body { width: 800px; height: 1200px; overflow: hidden; background: #ffffff; }
  .label {
    position: relative;
    width: 800px;
    height: 1200px;
    background: var(--label-yellow);
    overflow: hidden;
    font-family: "Oswald", sans-serif;
  }
  .comb {
    position: absolute;
    background: radial-gradient(closest-side, var(--comb-light), rgba(253, 214, 144, 0));
  }
  .comb--top-left { left: -120px; top: -100px; width: 360px; height: 320px; }
  .comb--top-right { right: -120px; top: -100px; width: 420px; height: 360px; }
  .comb--bottom-left { left: -160px; bottom: -140px; width: 520px; height: 600px; }
  .comb--bottom-right { right: -160px; bottom: -140px; width: 520px; height: 620px; }
  .frame { position: absolute; inset: 0; }
  .illustration {
    position: absolute;
    left: 110px;
    top: -20px;
    width: 580px;
    height: 470px;
    background:
      radial-gradient(ellipse 46% 40% at 50% 86%, var(--art-warm), rgba(233, 160, 74, 0)),
      radial-gradient(closest-side at 22% 68%, var(--art-soft), rgba(246, 185, 96, 0)),
      radial-gradient(closest-side at 78% 58%, var(--art-soft), rgba(246, 185, 96, 0)),
      radial-gradient(ellipse 8% 60% at 48% 35%, var(--art-warm), rgba(233, 160, 74, 0));
  }
  .title {
    position: absolute;
    left: 0;
    width: 800px;
    text-align: center;
    color: var(--honey-brown);
  }
  .title--script {
    top: 444px;
    font-family: "Lobster", cursive;
    font-weight: 400;
    font-size: 104px;
    line-height: 1;
  }
  .title--block {
    top: 550px;
    font-weight: 600;
    font-size: 188px;
    line-height: 1;
    letter-spacing: 2px;
  }
  .rule {
    position: absolute;
    left: 150px;
    top: 776px;
    width: 500px;
    height: 3px;
    background: var(--frame-white);
  }
  .tagline {
    position: absolute;
    top: 794px;
    left: 0;
    width: 800px;
    text-align: center;
    font-weight: 400;
    font-size: 36px;
    line-height: 44px;
    color: var(--ink-brown);
    letter-spacing: 0.5px;
  }
  .ribbon { position: absolute; left: 100px; top: 852px; width: 600px; height: 84px; }
  .ribbon-text {
    position: absolute;
    left: 0;
    top: 852px;
    width: 800px;
    height: 84px;
    line-height: 84px;
    text-align: center;
    color: #ffffff;
    font-weight: 700;
    font-size: 60px;
    letter-spacing: 20px;
    padding-left: 20px;
  }
  .maker {
    position: absolute;
    top: 1010px;
    left: 0;
    width: 800px;
    display: flex;
    align-items: center;
    justify-content: center;
    gap: 14px;
    color: var(--ink-brown);
    font-weight: 500;
    font-size: 30px;
    line-height: 40px;
    letter-spacing: 1px;
  }
  .maker-dot { width: 22px; height: 22px; border-radius: 50%; background: var(--ink-brown); }
</style>
</head>
<body>
  <div class="label">
    <div class="comb comb--top-left" role="img" aria-label="Faint honeycomb pattern"></div>
    <div class="comb comb--top-right" role="img" aria-label="Faint honeycomb pattern"></div>
    <div class="comb comb--bottom-left" role="img" aria-label="Faint honeycomb pattern"></div>
    <div class="comb comb--bottom-right" role="img" aria-label="Faint honeycomb pattern"></div>

    <svg class="frame" width="800" height="1200" viewBox="0 0 800 1200" aria-hidden="true">
      <path d="M56 20 H744 A36 36 0 0 0 780 56 V1144 A36 36 0 0 0 744 1180 H56 A36 36 0 0 0 20 1144 V56 A36 36 0 0 0 56 20 Z"
            fill="none" stroke="var(--frame-white)" stroke-width="3"/>
    </svg>

    <div class="illustration" role="img" aria-label="Illustration of a honey dipper dripping honey into a pool between two wildflowers, with bees flying around"></div>

    <h1 class="title title--script">Wildflower</h1>
    <div class="title title--block">HONEY</div>

    <div class="rule"></div>
    <p class="tagline">100% PURE &amp; UNFILTERED</p>

    <svg class="ribbon" width="600" height="84" viewBox="0 0 600 84" aria-hidden="true">
      <path d="M0 0 H600 L576 42 L600 84 H0 L24 42 Z" fill="var(--ribbon-brown)"/>
    </svg>
    <div class="ribbon-text">FLORIDA</div>

    <div class="maker">
      <span class="maker-dot"></span>
      <span>Sunmeadow Apiary</span>
    </div>
  </div>
</body>
</html>
```